design a beautiful, neat and professional looking 10 page templete for an online course

I designed an online course. It about the newborn adoption process. I need you to design the template for it. Just the first 10 pages is enough. I'm thinking a neutral palette with a pop of a minor color to keep it from being boring. The pop of color should not distract the reader. You can design how you want. If you want to add small details or hearts or a shape in background you can. Just dont overdo it. Sparingly is the key. You can make pages a different color. It just needs to look like a neutral color palette with a small pop of color.
Updates

Low design quality

Target Market(s)

people who are adopting a newborn in the USA

Industry/Entity Type

newborn adoption

Font styles to use
Sans Serif

Colors

Designer to choose colors to be used in the design.

Requirements
Should not have
• bold or distracting colors or patterns

```html
<!DOCTYPE html>
<html lang="en">
<head>
<meta charset="UTF-8">
<title>Newborn Adoption Course – Slide Templates</title>
<link href="https://fonts.googleapis.com/css2?family=Nunito:wght@400;600;700;800;900&display=swap" rel="stylesheet">
<style>
  :root{
    --stage:#282428;
    --paper:#ffffff;
    --cream:#fcf6ef;
    --sand:#ddcfc5;
    --sand-soft:#e0d3ca;
    --mist:#ececec;
    --slate:#5a6870;
    --ink:#4a4f53;
    --sun:#f2bd35;
  }
  *{margin:0;padding:0;box-sizing:border-box}
  html,body{width:1200px;height:1200px;overflow:hidden;background:var(--stage)}
  body{position:relative;font-family:"Nunito",sans-serif;color:var(--ink)}
  .slide{position:absolute;width:691px;height:388px;overflow:hidden;background:var(--paper)}
  .slide--about{left:68px;top:86px}
  .slide--services{left:312px;top:406px}
  .slide--best{left:456px;top:738px;background:var(--cream)}
  .shape{position:absolute;left:0;top:0}
  .eyebrow{position:absolute;font-size:6.5px;font-weight:700;letter-spacing:.6px;color:var(--slate);text-transform:uppercase}
  .heading{position:absolute;font-size:17px;font-weight:800;color:var(--slate);white-space:nowrap}
  .body{position:absolute;font-size:8.2px;line-height:15.5px;color:var(--ink)}
  .badge{position:absolute;background:var(--sand);border-radius:50%;color:#fff;text-align:center;display:flex;flex-direction:column;justify-content:center}
  .badge__num{font-size:17px;font-weight:900;line-height:1}
  .badge__label{font-size:8px;font-weight:800;margin-top:3px}
  .stat{position:absolute;top:256px;color:var(--slate);font-weight:800}
  .stat__num{font-size:13px;display:block}
  .stat__label{font-size:8.5px;display:block;margin-top:3px}
  .center{left:0;width:100%;text-align:center}
  .card{position:absolute;top:117px;width:125px;height:186px;border-radius:63px;background:#fff;box-shadow:0 4px 18px rgba(200,170,140,.18);text-align:center}
  .card__num{position:absolute;left:40px;top:40px;width:45px;height:45px;border-radius:50%;background:var(--slate);color:#fff;font-size:8px;font-weight:800;line-height:45px}
  .card__title{position:absolute;left:0;width:100%;top:100px;font-size:10px;font-weight:800;color:var(--slate)}
  .card__text{position:absolute;left:0;width:100%;top:119px;font-size:8px;line-height:15.5px;color:var(--ink)}
</style>
</head>
<body>

<!-- About -->
<section class="slide slide--about">
  <svg class="shape" width="691" height="388" viewBox="0 0 691 388">
    <path d="M0 0 H338 C385 25 392 110 362 152 C320 205 250 195 180 172 C110 150 60 200 0 213 Z" fill="var(--sand)"/>
    <path d="M648 355 C660 335 680 328 691 330 V388 H640 Z" fill="var(--mist)"/>
    <defs>
      <linearGradient id="momGlow" x1="0" y1="0" x2="1" y2="1">
        <stop offset="0" stop-color="#f4f1ef"/><stop offset=".5" stop-color="#ecc3c6"/><stop offset="1" stop-color="#d9a58c"/>
      </linearGradient>
      <linearGradient id="babyGlow" x1="0" y1="0" x2="0" y2="1">
        <stop offset="0" stop-color="#b8a79b"/><stop offset=".55" stop-color="#e8c1ad"/><stop offset="1" stop-color="#b7a0d6"/>
      </linearGradient>
    </defs>
    <path d="M269 93 C295 120 320 154 314 185 C305 230 268 248 244 275 C200 330 140 320 110 300 C85 285 80 240 100 210 C130 165 170 150 205 120 C230 100 250 85 269 93 Z" fill="none" stroke="var(--sun)" stroke-width="1.2" transform="translate(6 -3)"/>
    <g role="img" aria-label="Photo of a mother holding her newborn wrapped in a pink blanket">
      <path d="M150 36 C200 28 250 60 250 120 C250 170 215 200 180 240 C150 270 110 275 80 260 C45 242 28 200 38 165 C50 120 95 60 150 36 Z" fill="url(#momGlow)"/>
    </g>
    <g role="img" aria-label="Photo of a smiling baby in a lilac top">
      <path d="M269 93 C295 110 312 150 306 180 C298 220 266 246 244 270 C205 310 150 305 132 270 C118 240 130 200 160 168 C190 135 220 100 269 93 Z" fill="url(#babyGlow)"/>
    </g>
  </svg>
  <div class="badge" style="left:170px;top:247px;width:90px;height:90px">
    <span class="badge__num">320</span><span class="badge__label">Title Your Here</span>
  </div>
  <p class="eyebrow" style="left:450px;top:80px">About Us</p>
  <h2 class="heading" style="left:450px;top:95px">Information</h2>
  <p class="body" style="left:450px;top:127px;width:190px">Lorem ipsum dolor sit amet, consecte pricing turasanu adipiscing elit, sed dolor sita huasa eiusmod tempor incididunt ut labore et dolore magna its aliqual orci eu lobortis it elementum nibu eiusmod special. Lorem ipsum dolor sit amet, consecte pricing turasanu adipiscing elit, sed dolor sita huasa eiusmod tempor</p>
</section>

<!-- Our Services -->
<section class="slide slide--services">
  <svg class="shape" width="691" height="388" viewBox="0 0 691 388">
    <defs>
      <linearGradient id="newbornGlow" x1="0" y1="0" x2="1" y2="1">
        <stop offset="0" stop-color="#f7f6f5"/><stop offset=".55" stop-color="#ece7e4"/><stop offset="1" stop-color="#e7b9a0"/>
      </linearGradient>
    </defs>
    <path d="M348 0 C395 50 412 90 412 130 C410 160 380 180 320 178 C250 176 200 230 155 290 C120 330 70 342 0 340 V0 Z" fill="var(--sand-soft)"/>
    <path d="M0 296 C40 300 60 330 80 340 C110 340 120 360 105 388 H0 Z" fill="var(--mist)"/>
    <path d="M620 75 C660 70 691 100 691 120 V333 H520 Z" fill="#f2f2f2"/>
    <g role="img" aria-label="Photo of a sleeping newborn swaddled in a white blanket, cradled by hands">
      <path d="M400 132 C450 125 540 135 600 160 C650 180 691 175 691 175 V333 H335 C315 300 308 240 320 200 C335 160 365 138 400 132 Z" fill="url(#newbornGlow)"/>
    </g>
  </svg>
  <div class="badge" style="left:426px;top:39px;width:122px;height:90px;border-radius:50% 50% 48% 52%/55% 50% 50% 45%">
    <span class="badge__num">2500</span><span class="badge__label">Total Newborn</span>
  </div>
  <p class="eyebrow" style="left:55px;top:68px">Services</p>
  <h2 class="heading" style="left:55px;top:83px">Our Services</h2>
  <p class="body" style="left:55px;top:122px;width:220px">Lorem ipsum dolor sit amet, consecte pricing turasanu adipiscing elit, sed dolor sita huasa eiusmod tempor incididunt ut labore et dolore magna its aliqual orci eu lobortis it elementum nibu eiusmod special. Lorem ipsum dolor sit amet, consecte pricing turasanu adipiscing elit, sed dolor sita huasa eiusmod tempor</p>
  <div class="stat" style="left:55px"><span class="stat__num">750+</span><span class="stat__label">Title Your Here</span></div>
  <div class="stat" style="left:130px"><span class="stat__num">150+</span><span class="stat__label">Title Your Here</span></div>
  <div class="stat" style="left:206px"><span class="stat__num">1250+</span><span class="stat__label">Title Your Here</span></div>
</section>

<!-- Providing the Best Service -->
<section class="slide slide--best">
  <svg class="shape" width="691" height="388" viewBox="0 0 691 388">
    <path d="M349 0 C395 50 418 100 411 150 C405 180 370 185 330 180 C260 170 200 180 160 240 C120 300 60 340 0 340 V0 Z" fill="var(--sand-soft)"/>
  </svg>
  <p class="eyebrow center" style="top:30px">Services</p>
  <h2 class="heading center" style="top:45px">Providing the Best Service</h2>
  <article class="card" style="left:61px"><span class="card__num">01</span><h3 class="card__title">Title Your Here</h3><p class="card__text">Lorem ipsum dolor sit<br>amet dolor sit</p></article>
  <article class="card" style="left:209px"><span class="card__num">02</span><h3 class="card__title">Title Your Here</h3><p class="card__text">Lorem ipsum dolor sit<br>amet dolor sit</p></article>
  <article class="card" style="left:357px"><span class="card__num">03</span><h3 class="card__title">Title Your Here</h3><p class="card__text">Lorem ipsum dolor sit<br>amet dolor sit</p></article>
  <article class="card" style="left:505px"><span class="card__num">04</span><h3 class="card__title">Title Your Here</h3><p class="card__text">Lorem ipsum dolor sit<br>amet dolor sit</p></article>
  <p class="body center" style="top:330px">Lorem ipsum dolor sit amet, consecte pricing turasanu adipiscing elit, sed dolor sita huasa eiusmod tempor incididunt ut labore<br>et dolore magna its aliqual orci eu lobortis it elementum nibu eiusmod special</p>
</section>

</body>
</html>
```